Manufacturing company needs new business card.

I need a unique Business Card that will truly stand out. Nothing too busy. Simple is good, right? Not looking for a standard design either. No cookie cutter layout. I am just looking for something interesting and a bit different. Does't have to completely off the wall crazy, just not your run of the mill business card. Clean and modern with a touch of industrial.

Target Market(s)

Air conditioning industry, Architects, builders.

Industry/Entity Type

Business

Contact Information for Business Card

Details to be included on card are:

Peter Walsh
Managing Director

T: 1300 418 592
M: 0427 385 914
W: www.brandvalefabrication.com.au
E: peter.walsh@brandvalefabrication.com.au
A: 58 Harlow Lane, Sydney NSW 2000

Font styles to use
Sans Serif

Colors
0355a3
848484
fbfbfb

Requirements
Must have
• Card design must be landscape.

```html
<!DOCTYPE html>
<html lang="en">
<head>
<meta charset="utf-8">
<title>Brandvale Fabrication – Business Card</title>
<link rel="stylesheet" href="https://fonts.googleapis.com/css2?family=Karla:wght@400;500;700&display=swap">
<style>
  :root {
    --brand-blue: #3157a3;
    --brand-grey: #848484;
    --paper: #fbfbfb;
    --ink: #2a2a2a;
    --backdrop: #e9e7e3;
  }
  * { box-sizing: border-box; margin: 0; padding: 0; }
  html, body {
    width: 1200px;
    height: 1200px;
    overflow: hidden;
  }
  body {
    background: var(--backdrop);
    font-family: "Karla", Arial, sans-serif;
    color: var(--ink);
    position: relative;
  }
  .card {
    position: absolute;
    left: 210px;
    width: 780px;
    height: 470px;
    box-shadow: 0 6px 18px rgba(0,0,0,0.14);
  }
  /* Front */
  .card-front {
    top: 70px;
    background: var(--brand-blue);
    display: flex;
    align-items: center;
    justify-content: center;
  }
  .brand-plate {
    width: 560px;
    height: 150px;
    background: var(--paper);
    display: flex;
    align-items: center;
    justify-content: center;
    gap: 22px;
  }
  .brand-square {
    width: 44px;
    height: 44px;
    background: var(--brand-blue);
  }
  .brand-name {
    font-size: 40px;
    font-weight: 700;
    color: var(--brand-blue);
    letter-spacing: -0.3px;
  }
  /* Back */
  .card-back {
    top: 630px;
    background: var(--paper);
    text-align: center;
  }
  .side-block {
    position: absolute;
    top: 156px;
    width: 110px;
    height: 158px;
    background: var(--brand-blue);
  }
  .side-block.left { left: 0; }
  .side-block.right { right: 0; }
  .label {
    color: var(--brand-blue);
    font-weight: 700;
  }
  .phones {
    position: absolute;
    top: 96px;
    left: 0; right: 0;
    font-size: 23px;
  }
  .person {
    position: absolute;
    top: 192px;
    left: 0; right: 0;
  }
  .person-name {
    font-size: 36px;
    font-weight: 700;
    color: var(--brand-blue);
    letter-spacing: 0.5px;
  }
  .person-title {
    font-size: 23px;
    margin-top: 4px;
  }
  .contact-lines {
    position: absolute;
    top: 350px;
    left: 0; right: 0;
    font-size: 22px;
    line-height: 30px;
    list-style: none;
  }
</style>
</head>
<body>
  <section class="card card-front" aria-label="Card front">
    <div class="brand-plate">
      <span class="brand-square"></span>
      <span class="brand-name">Brandvale Fabrication</span>
    </div>
  </section>

  <section class="card card-back" aria-label="Card back">
    <p class="phones"><span class="label">T:</span> 1300 418 592, <span class="label">M:</span> 0427 385 914</p>
    <span class="side-block left"></span>
    <span class="side-block right"></span>
    <div class="person">
      <h1 class="person-name">Peter Walsh</h1>
      <p class="person-title">Managing Director</p>
    </div>
    <ul class="contact-lines">
      <li><span class="label">W:</span> www.brandvalefabrication.com.au</li>
      <li><span class="label">E:</span> peter.walsh@brandvalefabrication.com.au</li>
      <li><span class="label">A:</span> 58 Harlow Lane, Sydney NSW 2000</li>
    </ul>
  </section>
</body>
</html>
```